"Brightwall Sound Living Residences" need a busines Card Design got Builder

We need a business card design for a company based in Milford, Michigancalled Brightwall Sound Living Residences - has been recognized as a premier custom home builder. Distinguished by outstanding craftmanship and timeless beauty. Our custom home can be found in the most prestigious communities in Michigan. The homes are built with ICF (insulated concrete homes) which is green, allergy free, fire free, mold free and quitter. Our slogan "building one dream at a Time" and also we are ICF distributor for the state of Michigan

Target Market(s)

Anyone who is making over $100,000 a year and who wants to have totally custom built home. Ages from 29 up to 60 years old

Industry/Entity Type

Concrete

Contact Information for Business Card

we want to use - green, black, gray or blue colors - we want to look different with our business cards, because we built homes only with ICF, green, healthier and highly energy efficient homes.

Requirements
Must have
• I have logo that I attached and we have been using the logo (the only green home)
Nice to have
• should look quality business card,

Files

```html
<!DOCTYPE html>
<html lang="en">
<head>
<meta charset="utf-8">
<title>Brightwall Sound Living Residences – Business Card</title>
<link href="https://fonts.googleapis.com/css2?family=Arimo:wght@400;700&display=swap" rel="stylesheet">
<style>
  :root {
    --backdrop: #e9e9e6;
    --card: #ffffff;
    --green: #9ccc3c;
    --green-light: #d6eaa2;
    --green-deep: #86bb2a;
    --ink: #7c7c7c;
    --ink-soft: #a9a9a9;
  }
  * { margin: 0; padding: 0; box-sizing: border-box; }
  html, body {
    width: 1200px; height: 885px; overflow: hidden;
    background: var(--backdrop);
    font-family: "Arimo", Arial, sans-serif;
  }
  .card {
    position: absolute; left: 120px; top: 168px;
    width: 960px; height: 549px;
    background: var(--card);
    box-shadow: 0 18px 40px rgba(0,0,0,0.18);
    overflow: hidden;
  }
  .card__band { position: absolute; inset: 0; }
  .card__mark {
    position: absolute; left: 92px; top: 62px;
    width: 128px; height: 128px; border-radius: 50%;
    background: var(--green); border: 8px solid var(--card);
  }
  .card__since {
    position: absolute; right: 46px; top: 38px;
    text-align: right; color: var(--green-deep);
    font-size: 14px; letter-spacing: 0.5px; line-height: 1.35;
    text-transform: uppercase;
  }
  .brand {
    position: absolute; left: 250px; top: 88px;
  }
  .brand__name {
    color: var(--ink-soft); font-weight: 400;
    font-size: 36px; line-height: 1.0; letter-spacing: 2px;
    text-transform: uppercase;
  }
  .brand__slogan {
    margin-top: 10px; color: var(--green); font-size: 22px;
  }
  .person { position: absolute; left: 250px; top: 262px; }
  .person__name { color: var(--ink); font-weight: 700; font-size: 30px; }
  .person__role { color: var(--ink-soft); font-size: 19px; margin-top: 6px; }
  .card__rule {
    position: absolute; left: 250px; top: 358px;
    width: 660px; height: 2px; background: var(--green);
  }
  .card__rule-end {
    position: absolute; right: 50px; top: 250px;
    width: 2px; height: 110px; background: var(--green);
  }
  .contact {
    position: absolute; left: 250px; top: 392px;
    list-style: none; color: var(--ink); font-size: 20px; line-height: 38px;
  }
  .contact__item { display: flex; align-items: center; gap: 12px; }
  .contact__icon { width: 18px; height: 18px; }
  .address {
    position: absolute; right: 50px; top: 392px;
    text-align: right; color: var(--ink); font-size: 20px; line-height: 30px;
    font-style: normal;
  }
</style>
</head>
<body>
  <div class="card">
    <svg class="card__band" width="960" height="549" viewBox="0 0 960 549" aria-hidden="true">
      <defs>
        <linearGradient id="bandFill" x1="0" y1="0" x2="1" y2="0">
          <stop offset="0" stop-color="#9ccc3c"/>
          <stop offset="1" stop-color="#d6eaa2"/>
        </linearGradient>
      </defs>
      <polygon points="0,0 150,0 215,549 0,549" fill="url(#bandFill)"/>
      <line x1="150" y1="0" x2="215" y2="549" stroke="#ffffff" stroke-width="3"/>
    </svg>

    <div class="card__mark" aria-hidden="true"></div>

    <p class="card__since">Building insulated concrete form<br>(ICF) homes since 1999</p>

    <div class="brand">
      <h1 class="brand__name">Brightwall Sound<br>Living Residences</h1>
      <p class="brand__slogan">building one dream at a Time</p>
    </div>

    <div class="person">
      <p class="person__name">Employee Name</p>
      <p class="person__role">Managing Director</p>
    </div>

    <div class="card__rule"></div>
    <div class="card__rule-end"></div>

    <ul class="contact">
      <li class="contact__item">
        <svg class="contact__icon" viewBox="0 0 18 18" aria-hidden="true"><rect width="18" height="18" rx="3" fill="#7c7c7c"/><path d="M5 4c1 0 1.5 2 1.6 3 0 .6-.8.9-.6 1.5.5 1.2 1.3 2 2.5 2.5.6.2.9-.6 1.5-.6 1 .1 3 .6 3 1.6 0 1-1 2-2 2C7 14 4 11 4 6c0-1 .5-2 1-2z" fill="#fff"/></svg>
        248-555-0142
      </li>
      <li class="contact__item">
        <svg class="contact__icon" viewBox="0 0 18 18" aria-hidden="true"><rect width="18" height="18" rx="3" fill="#7c7c7c"/><path d="M5 4c1 0 1.5 2 1.6 3 0 .6-.8.9-.6 1.5.5 1.2 1.3 2 2.5 2.5.6.2.9-.6 1.5-.6 1 .1 3 .6 3 1.6 0 1-1 2-2 2C7 14 4 11 4 6c0-1 .5-2 1-2z" fill="#fff"/></svg>
        772-555-0187
      </li>
    </ul>

    <address class="address">742 Orchard Ridge Road 210, Milford<br>MI 48380, United States</address>
  </div>
</body>
</html>
```